Envelope design

We need a envelope design for a professional services firm called Brindlemoor Tax Advisory Inc. The firm is essentially a very specialized tax accounting firm - instead of serving the end consumer, we support other public accounting firms in the area of Canadian and U.S. tax advisory and compliance (i.e. they call us on tax issues too complex for the general practitioner). Our byline is "Tax Support Services for Public Accounting Firms". Our postcard should utilize our logo and be based on colours present in our logo (see file attached). The final design needs to convey professionalism and trustworthiness (we're hired by accountants after all!) while being creative and eye-catching. Eye-catching is critical, since many prospective recipients will not have heard from me before and I want them to read the postcard.
At lot of design work has already been done here. I've attached a number of sample files showing logo and letterhead designs. Please note that the letterhead hasn't yet been updated for the new logo. This is happening in a separate design competition.
Updates
Project Deadline Extended Reason: Deadline is extended because I am pricing the extra cost of having colour right to the edge of the envelopes. This will help me design on final design. Pricing should come in on Monday. Added Saturday, February 20, 2016

```html
<!DOCTYPE html>
<html lang="en">
<head>
<meta charset="utf-8">
<title>Brindlemoor Tax Advisory Inc. — Envelope Set</title>
<link href="https://fonts.googleapis.com/css2?family=Cinzel:wght@400&family=Open+Sans:wght@400&display=swap" rel="stylesheet">
<style>
  :root {
    --backdrop: #b9b9b9;
    --paper: #ffffff;
    --orange: #f15a27;
    --amber: #f7bd32;
    --navy: #1f3566;
    --ink: #1d1d1d;
    --muted: #555555;
  }
  * { margin: 0; padding: 0; box-sizing: border-box; }
  html, body { width: 842px; height: 1200px; overflow: hidden; }
  body { background: var(--backdrop); position: relative; font-family: "Open Sans", Arial, sans-serif; }

  .envelope {
    position: absolute; left: 74px; width: 694px; height: 301px;
    background: var(--paper);
    box-shadow: 0 3px 10px rgba(0,0,0,0.28);
    overflow: hidden;
  }
  .envelope--front-compact { top: 74px; }
  .envelope--front-feature { top: 450px; }
  .envelope--back { top: 825px; }

  .header-band {
    position: absolute; left: 0; top: 0; width: 100%; height: 56px;
    background: linear-gradient(90deg, #f04e23 0%, #f5962e 30%, #f7bd32 50%, #f4962c 72%, #f04e23 100%);
  }

  .return-address {
    position: absolute; left: 28px; top: 12px;
    color: #fff; font-size: 10px; line-height: 13px; font-style: normal;
  }

  .brand-text { display: inline-block; }
  .brand-name {
    font-family: "Cinzel", Georgia, serif; font-weight: 400;
    color: var(--ink); white-space: nowrap;
  }
  .brand-tagline {
    font-family: "Cinzel", Georgia, serif; color: var(--muted);
    white-space: nowrap; text-transform: uppercase;
    border-top: 1px solid #9a9a9a;
    text-align: justify; text-align-last: justify;
  }
  .brand-mark { position: absolute; background: var(--navy); }

  .lockup-compact { position: absolute; left: 14px; top: 86px; }
  .lockup-compact .brand-mark { left: 0; top: 3px; width: 28px; height: 28px; }
  .lockup-compact .brand-text { position: absolute; left: 36px; top: 0; }
  .lockup-compact .brand-name { font-size: 17px; line-height: 21px; }
  .lockup-compact .brand-tagline { font-size: 8px; padding-top: 2px; }

  .lockup-feature { position: absolute; left: 28px; top: 126px; }
  .lockup-feature .brand-mark { left: 80px; top: 0; width: 67px; height: 67px; }
  .lockup-feature .brand-text { position: absolute; left: 0; top: 72px; }
  .lockup-feature .brand-name { font-size: 15px; line-height: 18px; }
  .lockup-feature .brand-tagline { font-size: 6.5px; padding-top: 1px; }

  .flap {
    position: absolute; left: 0; top: 0; width: 694px; height: 112px;
    background: linear-gradient(180deg, #2a2a2a, #111111);
    clip-path: polygon(0 0, 100% 0, 96% 100%, 4% 100%);
  }
  .flap-mark {
    position: absolute; left: 333px; top: 16px; width: 28px; height: 28px;
    background: var(--amber);
  }
  .flap-name {
    position: absolute; left: 0; width: 694px; top: 54px; text-align: center;
    font-family: "Cinzel", Georgia, serif; color: #fff; font-size: 13px; letter-spacing: 0.8px;
  }
  .flap-web {
    position: absolute; left: 0; width: 694px; top: 80px; text-align: center;
    font-family: "Cinzel", Georgia, serif; color: #fff; font-size: 12px; letter-spacing: 0.8px;
  }
</style>
</head>
<body>

<section class="envelope envelope--front-compact">
  <div class="header-band" role="img" aria-label="Orange and amber header band"></div>
  <address class="return-address">418 Corran Street, Unit 7<br>Westhaven, Nova Scotia&nbsp; B4C 2K6</address>
  <div class="lockup-compact">
    <span class="brand-mark"></span>
    <div class="brand-text">
      <div class="brand-name">BRINDLEMOOR TAX ADVISORY INC.</div>
      <div class="brand-tagline">Tax support for public accounting firms</div>
    </div>
  </div>
</section>

<section class="envelope envelope--front-feature">
  <div class="header-band" role="img" aria-label="Orange and amber header band"></div>
  <address class="return-address">418 Corran Street, Unit 7<br>Westhaven, Nova Scotia&nbsp; B4C 2K6</address>
  <div class="lockup-feature">
    <span class="brand-mark"></span>
    <div class="brand-text">
      <div class="brand-name">BRINDLEMOOR TAX ADVISORY INC.</div>
      <div class="brand-tagline">Tax support for public accounting firms</div>
    </div>
  </div>
</section>

<section class="envelope envelope--back">
  <div class="flap" role="img" aria-label="Dark leather-textured envelope flap"></div>
  <span class="flap-mark"></span>
  <div class="flap-name">BRINDLEMOOR TAX ADVISORY INC.</div>
  <div class="flap-web">WWW.BRINDLEMOORTAX.SERVICES</div>
</section>

</body>
</html>
```